Wellspring Renewal Collective Botswana Africa Flyer

Create an A5 double sided flyer to advertise a campus lifestyle wellness training at the university of Tselakgang. This flyer invite all interested to freely attend naturopathic treatment training, stop addiction training, music therapy training lessons. Conducted by Wellspring Renewal Collective. The lead facilitator is Marisol-Ann Okoye.
Flyer text available at 'must haves'

Target Market(s)

University students

Industry/Entity Type

Training

Requirements
Must have
• Logo (supplied)
• Picture of Marisol-Ann Okoye, our Lead Facilitator (supplied)
• Music pic. Classical hym choir or preferably orchestra of predominantly black youth
• And the text must be as follows:
• WELLSPRING RENEWAL COLLECTIVE (WRC) is a non profit organization that conducts wholistic health programs in Universities aimed at reversing Lifestyle Diseases and breaking down the chains of Drug Addiction and Satanism among the youth. We conduct a 3 hour practical training every week on disease treatment protocols, stop addiction and music therapy.
• 1. Disease Treatment Programs: We thoroughly train you to use food, herbs, natural remedies and scientifically proven lifestyle changes to reverse lifestyle diseases such as diabetes, arthritis, cancer and hypertension.
• 2. Stop Addiction Programs: We also teach you how to administer a 10 day treatment protocol to wipe out the craving for drugs such cocaine, marijuana and tobacco, and to also rehabilitate those freed from these addictions.
• 3. Music Therapy: Top notch musical training will equip you to efficiently administer music therapy to heal the soul and relief tensions in any community using voice and musical instruments. Music, when properly done, heals both the singer and the one to whom it is sung!
• These training protocols will not only help you but most importantly will equip you to effectively help others!
• THE MUSIC CONNECTION
• Music is part of our being. There is a kind of music that goes to the waist igniting in us the desire for illicit sex, drugs and all recklessness. And there is a type of music that touches the heart and bring us closer to our Maker, igniting feelings of sympathy, kindness and generosity to our fellow man.
• When we are happy, a song always says it best. When we are sad, music has a way of saying it in ways that words would never reach. And when there is a call to action, a cause to which the sleeping needs to be awakened, music makes a perfect wake up call!
• The cause of WRC is a liberation struggle that cannot do without music. For when the chains of addiction are broken down, the joy that comes cannot be expressed in talking tones. And since it was through music that our captivity was perpetuated, it's only befitting that our liberation must be sustained through song. It is a new song though, which we shall first learn to sing in voice, and then through musical instruments of harps, violins and keyboards. A Quadrangle Ensemble of Daybreak, singing Meadowlight Hymns! You ought to be a part of it!
• THIS VALUABLE TRAINING THAT IS WORTH LOTS OF MONEY ELSEWHERE IS NOW BROUGHT TO YOU FREE OF CHARGE. TO ENROLL IMMEDIATELY CALL 71450362 or EMAIL: WRC2016@kelvora.com

```html
<!DOCTYPE html>
<html lang="en">
<head>
<meta charset="utf-8">
<title>Wellspring Renewal Collective Flyer</title>
<link rel="stylesheet" href="https://fonts.googleapis.com/css2?family=Oswald:wght@600;700&family=Roboto+Condensed:wght@700&family=Lato:wght@400;700;900&display=swap">
<style>
  :root{
    --green:#1f9a1f;
    --green-box:#1a9a22;
    --red:#e0262b;
    --ink:#222;
    --paper:#ffffff;
    --backdrop:#e9e6e2;
    --photo-dark:#3a3a3c;
    --photo-skin:#b58d72;
    --photo-horse:#5a3424;
  }
  *{box-sizing:border-box;margin:0;padding:0}
  html,body{width:1200px;height:900px;overflow:hidden}
  body{background:var(--backdrop);position:relative;font-family:'Lato',sans-serif;color:var(--ink)}
  .flyer{position:absolute;background:var(--paper);overflow:hidden;box-shadow:0 4px 14px rgba(0,0,0,.25)}
  .flyer--front{left:103px;top:130px;width:452px;height:632px}
  .flyer--back{left:633px;top:130px;width:454px;height:635px}
  .flyer__shapes{position:absolute;inset:0;width:100%;height:100%}
  .brand{position:absolute;left:22px;top:40px;display:flex;align-items:center;gap:6px;width:150px}
  .brand__dot{width:22px;height:22px;border-radius:50%;background:var(--red);flex:none}
  .brand__name{font-family:'Lato',sans-serif;font-weight:900;font-size:10px;line-height:1.15;color:var(--green)}
  .photo{position:absolute;border-radius:50%;overflow:hidden}
  .photo--cello{left:227px;top:5px;width:220px;height:220px;background:radial-gradient(circle at 60% 45%,#6a6a6d,#2c2c2e 70%)}
  .photo--portrait{left:227px;top:5px;width:220px;height:220px;background:radial-gradient(circle at 50% 40%,#c9a58c,#6b4a38 60%,#d8d2c8 100%)}
  .photo--horses{position:absolute;left:236px;top:448px;width:216px;height:184px;border-radius:70px 0 0 0;background:linear-gradient(160deg,#3b2a22,var(--photo-horse) 45%,#2a2a2a 80%)}
  .title{position:absolute;left:28px;top:178px}
  .title__main{font-family:'Oswald',sans-serif;font-weight:700;font-size:40px;line-height:1;color:var(--green);letter-spacing:.5px}
  .title__sub{font-family:'Roboto Condensed',sans-serif;font-weight:700;font-size:19px;color:var(--red);letter-spacing:1px;margin-top:4px}
  .content{position:absolute;left:28px;font-size:10.2px;line-height:13.2px;text-align:justify}
  .heading{font-family:'Lato',sans-serif;font-weight:700;font-size:14px;color:var(--green);margin:6px 0 4px;display:flex;align-items:center;gap:6px;text-transform:uppercase}
  .heading__mark{width:8px;height:8px;background:var(--green);display:inline-block}
  .heading--plain{gap:0}
  .content p{margin-bottom:4px}
  .narrow{width:220px}
  .narrow-2{width:190px}
  .offer{position:absolute;left:0;top:497px;width:333px;height:138px;background:var(--green-box);border-radius:0 26px 0 0;padding:6px 0 0 22px;color:#111}
  .offer__lead{font-weight:700;font-size:10.6px;line-height:11.5px;text-transform:uppercase;text-align:justify;width:292px}
  .offer__call{font-weight:700;font-size:13.5px;margin-top:3px;letter-spacing:.3px}
  .contact{display:flex;align-items:center;gap:8px;margin-top:4px;font-weight:700;color:#111}
  .contact--phone{font-size:23px}
  .contact--mail{font-size:16px}
  .contact svg{flex:none}
</style>
</head>
<body>

<!-- Front side -->
<section class="flyer flyer--front">
  <svg class="flyer__shapes" viewBox="0 0 452 632" aria-hidden="true">
    <path d="M0 178 C60 120 140 60 235 0 L255 0 C160 70 80 140 0 198 Z" fill="var(--red)"/>
    <path d="M0 210 C80 150 170 90 250 40" fill="none" stroke="#d9d9d9" stroke-width="1.5"/>
    <path d="M452 180 C470 330 430 500 300 632 L340 632 C440 520 470 360 452 220 Z" fill="var(--red)"/>
    <circle cx="337" cy="115" r="114" fill="none" stroke="var(--red)" stroke-width="9"/>
  </svg>
  <div class="brand"><span class="brand__dot"></span><span class="brand__name">WELLSPRING RENEWAL COLLECTIVE</span></div>
  <div class="photo photo--cello" role="img" aria-label="Musician playing a cello on a dark background"></div>
  <div class="title">
    <div class="title__main">WELLSPRING</div>
    <div class="title__sub">RENEWAL COLLECTIVE</div>
  </div>
  <div class="content" style="top:262px;width:390px">
    <h2 class="heading heading--plain">Wellspring Renewal Collective (WRC)</h2>
    <p>is a non profit organization that conducts wholistic health programs in Universities aimed at reversing Lifestyle Diseases and breaking down the chains of Drug Addiction and Satanism among the youth. We conduct a 3 hour practical training every week on disease treatment protocols, stop addiction and music therapy.</p>
    <h2 class="heading"><span class="heading__mark"></span>Disease Treatment Programs</h2>
    <p>We thoroughly train you to use food, herbs, natural remedies and scientifically proven lifestyle changes to reverse lifestyle diseases such as diabetes, arthritis, cancer and hypertension.</p>
    <h2 class="heading"><span class="heading__mark"></span>Stop Addiction Programs</h2>
    <p class="narrow">We also teach you how to administer a 10 day treatment protocol to wipe out the craving for drugs such cocaine, marijuana and tobacco, and to also rehabilitate those freed from these addictions.</p>
    <h2 class="heading"><span class="heading__mark"></span>Music Therapy</h2>
    <p class="narrow-2">Top notch musical training will equip you to efficiently administer music therapy to heal the soul and relief tensions in any community using voice and musical instruments. Music, when properly done, heals both the singer and the one to whom it is sung!</p>
  </div>
  <div class="photo--horses" role="img" aria-label="Woman smiling beside two horses"></div>
</section>

<!-- Back side -->
<section class="flyer flyer--back">
  <svg class="flyer__shapes" viewBox="0 0 454 635" aria-hidden="true">
    <path d="M0 178 C60 120 140 60 235 0 L255 0 C160 70 80 140 0 198 Z" fill="var(--red)"/>
    <path d="M454 190 C470 360 440 520 333 635 L380 635 C460 530 475 370 454 230 Z" fill="var(--red)"/>
    <circle cx="337" cy="115" r="114" fill="none" stroke="var(--red)" stroke-width="9"/>
  </svg>
  <div class="brand"><span class="brand__dot"></span><span class="brand__name">WELLSPRING RENEWAL COLLECTIVE</span></div>
  <div class="photo photo--portrait" role="img" aria-label="Portrait of lead facilitator Marisol-Ann Okoye"></div>
  <div class="title">
    <div class="title__main">WELLSPRING</div>
    <div class="title__sub">RENEWAL COLLECTIVE</div>
  </div>
  <div class="content" style="top:262px;width:390px">
    <h2 class="heading"><span class="heading__mark"></span>The Music Connection</h2>
    <p>Music is part of our being. There is a kind of music that goes to the waist igniting in us the desire for illicit sex, drugs and all recklessness. And there is a type of music that touches the heart and bring us closer to our Maker, igniting feelings of sympathy, kindness and generosity to our fellow man.</p>
    <p>When we are happy, a song always says it best. When we are sad, music has a way of saying it in ways that words would never reach. And when there is a call to action, a cause to which the sleeping needs to be awakened, music makes a perfect wake up call!</p>
    <p>The cause of WRC is a liberation struggle that cannot do without music. For when the chains of addiction are broken down, the joy that comes cannot be expressed in talking tones. And since it was through music that our captivity was perpetuated, it's only befitting that our liberation must be sustained through song. It is a new song though, which we shall first learn to sing in voice, and then through musical instruments of harps, violins and keyboards. A Quadrangle Ensemble of Daybreak, singing Meadowlight Hymns! You ought to be a part of it!</p>
  </div>
  <div class="offer">
    <p class="offer__lead">This valuable training that is worth lots of money elsewhere is now brought to you free of charge.</p>
    <p class="offer__call">ENROLL IMMEDIATELY CALL</p>
    <p class="contact contact--phone">
      <svg width="16" height="18" viewBox="0 0 16 18" aria-hidden="true"><rect x="1" y="1" width="14" height="16" rx="3" fill="#111"/><path d="M5 4 C4 8 6 12 10 14 L11.5 12.5 L9.5 11 L8.5 12 C7 11 6 9 6 7.5 L7 6.5 L5.8 4.2 Z" fill="var(--green-box)"/></svg>
      71450362
    </p>
    <p class="contact contact--mail">
      <svg width="18" height="13" viewBox="0 0 18 13" aria-hidden="true"><rect width="18" height="13" fill="#111"/><path d="M0 0 L9 7 L18 0" fill="none" stroke="var(--green-box)" stroke-width="1.5"/></svg>
      WRC2016@kelvora.com
    </p>
  </div>
</section>

</body>
</html>
```